Bright Path Therapies business cards and stationary

Need business cards and stationary designed to match previously made logo for for a new company based in Sydney NSW called 'Bright Path Therapies'.

We provide early intervention services and diagnostic assessment for children with disability and their families. I would like designs that are colourful and child friendly - possibly using feet/footprints/steps on a white background. The final design should communicate that we are family friendly, accepting and fun to work with.

Target Market(s)

Parents and Families
Teachers
Allied Health Professionals

Industry/Entity Type

Psychology

Contact Information for Business Card

Bright Path Therapies
www.brightpaththerapies.example
info@brightpaththerapies.example

Font styles to use
Sans Serif
Decorative
Script

Requirements
Must have
• Match the font and colour scheme of logo, along with footprint picture
Nice to have
• Clean and simple, while reflecting that I am working with families.
• Also- editable for when we make staff specific cards.

```html
<!DOCTYPE html>
<html lang="en">
<head>
<meta charset="utf-8">
<title>Bright Path Therapies – Business Card</title>
<link rel="stylesheet" href="https://fonts.googleapis.com/css2?family=Open+Sans:ital,wght@0,400;0,700;1,400&display=swap">
<style>
  :root {
    --backdrop: #e6e7e8;
    --card: #ffffff;
    --brand-blue: #2a76b8;
    --text-blue: #3b7fc0;
    --mark-red: #ee4036;
    --step-green: #8cc640;
    --step-blue: #1f72bc;
    --step-red: #ef4136;
    --step-orange: #f7941d;
  }
  * { box-sizing: border-box; margin: 0; padding: 0; }
  html, body {
    width: 1200px; height: 562px; overflow: hidden;
    background: var(--backdrop);
    font-family: "Open Sans", Arial, sans-serif;
  }
  .canvas { position: relative; width: 1200px; height: 562px; }
  .card {
    position: absolute; top: 154px;
    width: 440px; height: 254px;
    background: var(--card);
    border-radius: 24px;
    overflow: hidden;
  }
  .card--front { left: 110px; }
  .card--back { left: 650px; }

  .brand {
    position: absolute; left: 0; right: 0; top: 98px;
    display: flex; align-items: center; justify-content: center; gap: 10px;
  }
  .brand__dot {
    width: 30px; height: 30px; border-radius: 50%;
    background: var(--mark-red);
  }
  .brand__name {
    font-size: 24px; font-weight: 400; color: var(--brand-blue);
    letter-spacing: 0.5px;
  }
  .tagline {
    position: absolute; left: 0; right: 0; top: 204px;
    text-align: center; font-size: 7.4px; color: var(--text-blue);
  }

  .footsteps {
    position: absolute; left: 20px; top: 0; width: 100px; height: 100%;
    background: linear-gradient(180deg,
      rgba(140,198,64,0.35) 0%, rgba(31,114,188,0.35) 20%,
      rgba(239,65,54,0.35) 38%, rgba(247,148,29,0.35) 56%,
      rgba(140,198,64,0.35) 72%, rgba(31,114,188,0.35) 86%,
      rgba(247,148,29,0.35) 100%);
  }
  .contact {
    position: absolute; right: 44px; top: 119px;
    text-align: right; color: var(--text-blue); font-size: 8px; line-height: 1.35;
  }
  .contact__name { font-weight: 700; font-size: 8.4px; }
  .contact__role { font-style: italic; }
  .contact__line {
    display: flex; align-items: center; justify-content: flex-end; gap: 6px;
  }
  .contact__phone { margin-top: 12px; }
  .contact__email { margin-top: 12px; }
  .contact__line svg { width: 8px; height: 8px; flex: none; }
</style>
</head>
<body>
<div class="canvas">
  <section class="card card--front">
    <div class="brand">
      <span class="brand__dot"></span>
      <span class="brand__name">Bright Path Therapies</span>
    </div>
    <p class="tagline">A Community of Passionate Therapists, Educators and Learners</p>
  </section>

  <section class="card card--back">
    <div class="footsteps" role="img" aria-label="Trail of colourful children's footprints in green, blue, red and orange walking down the card"></div>
    <div class="contact">
      <p class="contact__name">Alex Morgan</p>
      <p class="contact__role">Marketing Executive</p>
      <p class="contact__line contact__phone">
        <svg viewBox="0 0 16 16" aria-hidden="true"><path fill="currentColor" d="M3.6 1.2l2.3 2.6-1.3 1.8c.9 2 2.6 3.8 4.7 4.8l1.8-1.4 2.7 2.2-1.4 2.3C7.3 13.4 2.6 8.7 1.4 2.6z"/></svg>
        +61 2 5550 1234
      </p>
      <p class="contact__line contact__email">
        <svg viewBox="0 0 16 16" aria-hidden="true"><rect x="1" y="3" width="14" height="10" fill="none" stroke="currentColor" stroke-width="1.5"/><path d="M1 3l7 6 7-6" fill="none" stroke="currentColor" stroke-width="1.5"/></svg>
        info@brightpaththerapies.example
      </p>
      <p class="contact__line">
        <svg viewBox="0 0 16 16" aria-hidden="true"><circle cx="8" cy="8" r="7" fill="currentColor"/><path d="M1 8h14M8 1c3 3 3 11 0 14M8 1c-3 3-3 11 0 14" fill="none" stroke="#fff" stroke-width="1"/></svg>
        www.brightpaththerapies.example
      </p>
    </div>
  </section>
</div>
</body>
</html>
```